Halvorsen Partners Business Card

Halvorsen Partners Civil Construction
Marcus Halvorsen
CEO
727-518-6094
Marcus@HalvorsenSiteworks.example
www.HalvorsenSiteworks.example
Site Development
Utility Construction
Excavation
40876 County Lane 19
Land O' Lakes, FL 34638

Target Market(s)

Construction and government

Industry/Entity Type

Business

Contact Information for Business Card

I want an unique design that make a statement

Number of Pages Required

1 page

Font styles to use

Colors

Designer to choose colors to be used in the design.

Requirements
Must have
• unique design, feel free to modify or change the color of my logo.
Nice to have
• extra design features like spot UV, foil accents, color edges, unique paper, or any thing that would make my card pop.
• I like the feel of the image that I attached

```html
<!DOCTYPE html>
<html lang="en">
<head>
<meta charset="utf-8">
<title>Halvorsen Partners Business Card</title>
<link rel="stylesheet" href="https://fonts.googleapis.com/css2?family=Open+Sans:wght@400;600;700&display=swap">
<style>
  :root {
    --page: #e6e7ea;
    --card-white: #f7f7f8;
    --brand-blue: #203f8a;
    --brand-blue-deep: #1a3577;
    --ink-blue: #2e4f9e;
    --ink-grey: #6f7178;
    --on-blue: #ffffff;
    --rule-grey: #a7a9ae;
  }
  * { box-sizing: border-box; margin: 0; padding: 0; }
  html, body { width: 1200px; height: 960px; overflow: hidden; }
  body {
    background: var(--page);
    font-family: "Open Sans", Arial, sans-serif;
    position: relative;
  }
  .card {
    position: absolute;
    left: 250px;
    width: 700px;
    height: 400px;
    border-radius: 4px;
    box-shadow: 0 6px 18px rgba(0,0,0,0.18);
    overflow: hidden;
  }
  /* Front face */
  .card-front {
    top: 50px;
    background: var(--card-white);
    display: flex;
    align-items: center;
    justify-content: center;
  }
  .brand-lockup {
    display: flex;
    align-items: center;
    gap: 14px;
  }
  .brand-square {
    width: 44px;
    height: 44px;
    background: var(--ink-blue);
  }
  .brand-divider {
    width: 2px;
    height: 46px;
    background: var(--rule-grey);
  }
  .brand-name {
    color: var(--ink-blue);
    font-weight: 600;
    font-size: 27px;
    line-height: 1;
    letter-spacing: 0.5px;
    text-transform: uppercase;
  }
  .brand-tagline {
    color: var(--ink-grey);
    font-weight: 400;
    font-size: 13px;
    letter-spacing: 5.2px;
    text-transform: uppercase;
    margin-top: 6px;
  }
  /* Back face */
  .card-back {
    top: 510px;
    background: linear-gradient(135deg, var(--brand-blue) 0%, var(--brand-blue-deep) 100%);
    color: var(--on-blue);
  }
  .contact-block {
    position: absolute;
    left: 40px;
    top: 40px;
    width: 350px;
  }
  .company-name {
    font-weight: 700;
    font-size: 22px;
    line-height: 1;
    text-transform: uppercase;
  }
  .company-tagline {
    font-size: 10px;
    letter-spacing: 4.3px;
    text-transform: uppercase;
    margin-top: 4px;
  }
  .person-name {
    font-weight: 700;
    font-size: 18px;
    text-transform: uppercase;
    margin-top: 16px;
    line-height: 1.1;
  }
  .person-title {
    font-size: 14px;
    margin-bottom: 12px;
  }
  .contact-list, .service-list { list-style: none; }
  .contact-list li, .service-list li {
    display: flex;
    align-items: center;
    gap: 9px;
    font-size: 14.5px;
    line-height: 23px;
  }
  .contact-list svg { width: 13px; height: 13px; flex: none; fill: var(--on-blue); }
  .service-list li::before {
    content: "";
    width: 6px;
    height: 6px;
    background: var(--on-blue);
    flex: none;
    margin: 0 3px 0 3px;
  }
  .brand-panel {
    position: absolute;
    right: 40px;
    top: 40px;
    width: 300px;
    height: 320px;
    border: 26px solid var(--on-blue);
  }
</style>
</head>
<body>
  <section class="card card-front" aria-label="Card front">
    <div class="brand-lockup">
      <div class="brand-square"></div>
      <div class="brand-divider"></div>
      <div class="brand-text">
        <div class="brand-name">Halvorsen Partners</div>
        <div class="brand-tagline">Civil Construction</div>
      </div>
    </div>
  </section>

  <section class="card card-back" aria-label="Card back">
    <div class="contact-block">
      <div class="company-name">Halvorsen Partners</div>
      <div class="company-tagline">Civil Construction</div>
      <div class="person-name">Marcus Halvorsen</div>
      <div class="person-title">CEO</div>
      <ul class="contact-list">
        <li>
          <svg viewBox="0 0 16 16" aria-hidden="true"><path d="M3.6 1.2l2.3 2.4-1.2 2a9 9 0 0 0 5.7 5.7l2-1.2 2.4 2.3-1.4 2.4C7.6 14.6 1.4 8.4 1.2 2.6z"/></svg>
          727-518-6094
        </li>
        <li>
          <svg viewBox="0 0 16 16" aria-hidden="true"><path d="M1 3h14v10H1z M1.8 3.8L8 8.6l6.2-4.8" fill="none" stroke="#fff" stroke-width="1.6"/></svg>
          Marcus@HalvorsenSiteworks.example
        </li>
        <li>
          <svg viewBox="0 0 16 16" aria-hidden="true"><circle cx="8" cy="8" r="6.6" fill="none" stroke="#fff" stroke-width="1.5"/><path d="M1.4 8h13.2M8 1.4c-3 3.4-3 9.8 0 13.2M8 1.4c3 3.4 3 9.8 0 13.2" fill="none" stroke="#fff" stroke-width="1.2"/></svg>
          www.HalvorsenSiteworks.example
        </li>
      </ul>
      <ul class="service-list">
        <li>Site Development</li>
        <li>Excavation</li>
        <li>Utility Construction</li>
      </ul>
    </div>
    <div class="brand-panel" aria-hidden="true"></div>
  </section>
</body>
</html>
```